Wedding Vows Poster for a Frame (anniversary gift )

I need an 8 X11 copy of both or wedding vows that I can frame in a classy and timeless modern font to frame for our house .

see file attach for text (vows)

project is now close thank you for all your help

```html
<!DOCTYPE html>
<html lang="en">
<head>
<meta charset="utf-8">
<title>Wedding Vows Posters – Clara &amp; Daniel</title>
<link rel="stylesheet" href="https://fonts.googleapis.com/css2?family=Cinzel:wght@400&display=swap">
<style>
  :root {
    --page-bg: #f4f4f4;
    --paper: #ffffff;
    --ink: #111111;
    --flourish-grey: #c6c6c6;
    --ornament-dark: #1a1a1a;
    --shadow: rgba(0, 0, 0, 0.35);
  }
  * { box-sizing: border-box; margin: 0; padding: 0; }
  html, body {
    width: 1117px;
    height: 1200px;
    overflow: hidden;
    background: var(--page-bg);
  }
  .sheet {
    position: relative;
    width: 1117px;
    height: 1200px;
  }
  .vow-poster {
    position: absolute;
    top: 243px;
    width: 520px;
    height: 714px;
    background: var(--paper);
    box-shadow: 6px 8px 10px var(--shadow);
    font-family: 'Cinzel', Georgia, serif;
    color: var(--ink);
    overflow: hidden;
  }
  .vow-poster--clara { left: 26px; }
  .vow-poster--daniel { left: 571px; }

  .crest-ornament {
    position: absolute;
    top: 22px;
    width: 140px;
    height: 62px;
    border-radius: 50% 50% 30% 30%;
    background: radial-gradient(ellipse at center, var(--ornament-dark) 0%, #4a4a4a 45%, rgba(255,255,255,0) 72%);
    opacity: 0.8;
    z-index: 2;
  }
  .vow-poster--clara .crest-ornament { left: 62px; }
  .vow-poster--daniel .crest-ornament { left: 70px; }

  .side-flourish {
    position: absolute;
    border-radius: 45%;
    background: radial-gradient(ellipse at center, var(--flourish-grey) 0%, rgba(198,198,198,0.6) 45%, rgba(255,255,255,0) 72%);
  }
  .vow-poster--clara .side-flourish { top: 190px; left: 320px; width: 230px; height: 450px; }
  .vow-poster--daniel .side-flourish { top: 170px; left: 10px; width: 270px; height: 430px; }

  .title {
    position: absolute;
    display: flex;
    align-items: baseline;
    font-weight: 400;
    white-space: nowrap;
    z-index: 1;
  }
  .vow-poster--clara .title { top: 50px; left: 86px; }
  .vow-poster--daniel .title { top: 42px; left: 132px; }
  .title__initial { line-height: 0.72; }
  .vow-poster--clara .title__initial { font-size: 200px; }
  .vow-poster--daniel .title__initial { font-size: 160px; }
  .title__rest {
    font-size: 30px;
    line-height: 1;
    margin-left: -2px;
  }

  .vow-text {
    position: absolute;
    left: 0;
    right: 0;
    text-align: center;
    z-index: 1;
  }
  .vow-poster--clara .vow-text {
    top: 258px;
    padding: 0 4px 0 100px;
    font-size: 17.5px;
    line-height: 1.05;
  }
  .vow-poster--daniel .vow-text {
    top: 168px;
    padding: 0 6px 0 80px;
    font-size: 16px;
    line-height: 1.23;
  }
  .vow-poster--clara .vow-text p + p { margin-top: 20px; }
  .vow-poster--daniel .vow-text p + p { margin-top: 8px; }
  .vow-text .sign-off { font-size: 16px; }
  .vow-poster--clara .vow-text .sign-off { margin-top: 22px; }
  .vow-poster--daniel .vow-text .sign-off { margin-top: 18px; }
  .signature { display: block; font-size: 14px; margin-top: 2px; }
  .small-ornament {
    display: block;
    width: 30px;
    height: 10px;
    margin: 5px auto 0;
    border-radius: 50%;
    background: radial-gradient(ellipse at center, var(--ornament-dark) 0%, rgba(26,26,26,0.4) 60%, rgba(255,255,255,0) 80%);
  }
</style>
</head>
<body>
<main class="sheet">

  <article class="vow-poster vow-poster--clara">
    <div class="side-flourish" role="img" aria-label="Large grey decorative leaf flourish behind the vow text"></div>
    <div class="crest-ornament" role="img" aria-label="Black scroll ornament above the initial"></div>
    <h1 class="title"><span class="title__initial">C</span><span class="title__rest">lara to Daniel</span></h1>
    <div class="vow-text">
      <p>“This ring represents my commitment to<br>you as your partner and to our marriage.<br>As your partner I promise to always do my<br>best to support, respect, be compassionate<br>and loving to you. &nbsp;And as your wife, I<br>promise to always to my best to be honest,<br>trust worthy trust and during<br>challenging times to have the faith that<br>we will somehow overcome it and be even<br>stronger on the other side.</p>
      <p>Dani, you are my favorite person, I love<br>you with all my heart and I am so very<br>proud to be your wife.”</p>
      <p class="sign-off">Love always,<span class="signature">C</span><span class="small-ornament" role="img" aria-label="Small black ornament"></span></p>
    </div>
  </article>

  <article class="vow-poster vow-poster--daniel">
    <div class="side-flourish" role="img" aria-label="Large grey decorative leaf flourish behind the vow text"></div>
    <div class="crest-ornament" role="img" aria-label="Black scroll ornament above the initial"></div>
    <h1 class="title"><span class="title__initial">D</span><span class="title__rest">aniel to Clara</span></h1>
    <div class="vow-text">
      <p>Three years ago I fell in love with you on our<br>journey trough Peru,<br>your love for life , your drive, your beautiful<br>smile, and natural beauty were at the time<br>what got my attention.<br>Now that I know much more about you I have<br>realize how much more complete of an<br>individual you are.<br>For a long time I wish I had meet you before<br>however only now I can appreciate you fully.<br>I love you Clara<br>“This ring represents my commitment to you<br>as your partner and to our marriage.<br>As your partner I am committed to a life<br>where we can have it all. &nbsp;By all I mean an<br>amazing relationship where we can share a<br>fulfilling life together.<br>As your husband I promise to be loyal and give<br>you the best that I can, protect and cherish<br>you I will always be there for you trough<br>good and hard time.</p>
      <p>I will grow old with you and love you<br>forever.</p>
      <p class="sign-off"><span class="signature">Daniel</span><span class="small-ornament" role="img" aria-label="Small black ornament"></span></p>
    </div>
  </article>

</main>
</body>
</html>
```